Ridge Contracting LLC Business Card Design

I am looking for a creative and unique business card design. We are a commercial construction general contractor. With the name "RIDGE" Contracting, I am hoping to see some neat designs that correlate with the name.

```html
<!DOCTYPE html>
<html lang="en">
<head>
<meta charset="utf-8">
<title>Ridge Contracting LLC – Business Card</title>
<link href="https://fonts.googleapis.com/css2?family=Poppins:wght@400;500;800&display=swap" rel="stylesheet">
<style>
  :root {
    --backdrop: #3a3a3c;
    --card-white: #ffffff;
    --brand-blue: #1d86cf;
    --brand-blue-light: #36a6e2;
    --brand-blue-deep: #1672b8;
    --ink: #2b2b2b;
    --rule: #8cc6ec;
  }
  * { margin: 0; padding: 0; box-sizing: border-box; }
  html, body { width: 1200px; height: 689px; overflow: hidden; }
  body {
    background: var(--backdrop);
    font-family: "Poppins", sans-serif;
    display: flex;
    align-items: center;
    justify-content: center;
    gap: 60px;
  }
  .card {
    width: 500px;
    height: 286px;
    border-radius: 22px;
    position: relative;
    overflow: hidden;
    box-shadow: 0 18px 40px rgba(0,0,0,.45);
  }
  .card-front {
    background: linear-gradient(150deg, var(--brand-blue-deep) 0%, var(--brand-blue-light) 50%, var(--brand-blue) 100%);
    display: flex;
    align-items: center;
    justify-content: center;
  }
  .card-front .wordmark { color: #1b7cc4; }
  .wordmark {
    font-weight: 800;
    font-size: 44px;
    letter-spacing: 2px;
    line-height: 1;
    text-align: center;
  }
  .wordmark small {
    display: block;
    font-size: 14px;
    letter-spacing: 8px;
    margin-top: 8px;
  }
  .card-back {
    background: var(--card-white);
    border-bottom: 5px solid var(--brand-blue);
    display: flex;
    align-items: center;
    padding: 0 30px;
  }
  .card-back .wordmark {
    color: var(--brand-blue);
    width: 200px;
    flex: none;
    font-size: 38px;
  }
  .card-back .wordmark small { font-size: 12px; letter-spacing: 6px; }
  .divider {
    width: 1px;
    height: 170px;
    background: var(--rule);
    margin: 0 22px 0 16px;
    flex: none;
  }
  .details { color: var(--ink); font-size: 13px; line-height: 1.5; white-space: nowrap; }
  .person-name {
    color: var(--brand-blue);
    font-weight: 800;
    font-size: 20px;
    line-height: 1.1;
  }
  .person-role { font-size: 14px; margin-bottom: 12px; }
  .contact-list { list-style: none; margin-bottom: 10px; }
  .contact-list li { display: flex; align-items: center; gap: 7px; }
  .contact-list svg { width: 12px; height: 12px; fill: var(--brand-blue); flex: none; }
  .accent { color: var(--brand-blue); }
</style>
</head>
<body>
  <section class="card card-front" aria-label="Card front">
    <div class="wordmark">RIDGE<small>CONTRACTING</small></div>
  </section>

  <section class="card card-back" aria-label="Card back">
    <div class="wordmark">RIDGE<small>CONTRACTING</small></div>
    <div class="divider"></div>
    <div class="details">
      <p class="person-name">DANIEL MORROW</p>
      <p class="person-role">Managing Director</p>
      <ul class="contact-list">
        <li><svg viewBox="0 0 24 24"><path d="M6.6 10.8a15 15 0 0 0 6.6 6.6l2.2-2.2c.3-.3.7-.4 1-.2 1.1.4 2.3.6 3.6.6.6 0 1 .4 1 1V20c0 .6-.4 1-1 1A17 17 0 0 1 3 4c0-.6.4-1 1-1h3.5c.6 0 1 .4 1 1 0 1.3.2 2.5.6 3.6.1.3 0 .7-.2 1z"/></svg><span>044-987 650 312</span></li>
        <li><svg viewBox="0 0 24 24"><path d="M2 5h20v14H2zm2 2v.5l8 5 8-5V7l-8 5z"/></svg><span>office@ridgeco.com</span></li>
        <li><svg viewBox="0 0 24 24"><circle cx="12" cy="12" r="10"/></svg><span>www.<span class="accent">ridgebuilds</span>.com</span></li>
      </ul>
      <p>218 Granite Avenue, Suite 4<br>30814, Fairview County</p>
    </div>
  </section>
</body>
</html>
```